Call center Word Template for Business Proposals

We recently opened a Call Center that handles the customer service for financial institutions. We just got our logo and we need a Word template for our business proposals, this way we can make them look very professional. I am attaching all the files with our logo that may be needed.

Target Market(s)

Financial institutions

Industry/Entity Type

Call Center

Font styles to use
Serif
Sans Serif

Colors
0d5aa7
3176b5
85acd3
cedeed
eaf1f7
feeeee
fbd4d5
f59195
f04a50

Requirements
Nice to have
• Sleek modern design

```html
<!DOCTYPE html>
<html lang="en">
<head>
<meta charset="utf-8">
<title>Harbor Line — Business Proposal Template</title>
<link rel="stylesheet" href="https://fonts.googleapis.com/css2?family=Playfair+Display:wght@600;700&family=Open+Sans:wght@400;600;700&display=swap">
<style>
:root{
  --blue-900:#0d5aa7;
  --blue-700:#3176b5;
  --blue-400:#85acd3;
  --blue-200:#cedeed;
  --blue-100:#eaf1f7;
  --pink-050:#feeeee;
  --pink-200:#fbd4d5;
  --red-400:#f59195;
  --red-600:#f04a50;
  --ink:#4a5563;
  --muted:#98a2ad;
  --rule:#dfe5ec;
  --paper:#ffffff;
  --stage:#ffffff;
}
*{margin:0;padding:0;box-sizing:border-box}
html,body{width:1200px;height:252px;overflow:hidden;background:var(--stage)}
body{font-family:"Open Sans",Arial,sans-serif;color:var(--ink);position:relative}
.page{position:absolute;top:0;height:252px;background:var(--paper);overflow:hidden;box-shadow:0 0 0 .5px var(--rule)}
.cover{left:0;width:190px;background:linear-gradient(160deg,var(--blue-700) 0%,var(--blue-900) 70%);color:#fff}
.cover-band{position:absolute;left:0;right:0;bottom:0;height:6px;background:var(--red-600)}
.brand{position:absolute;left:16px;top:70px;font-size:6px;font-weight:700;letter-spacing:.4px;color:#fff}
.cover h1{position:absolute;left:16px;top:84px;width:150px;font-family:"Playfair Display",Georgia,serif;font-size:11.5px;line-height:1.25;font-weight:700}
.cover .lede{position:absolute;left:16px;top:122px;width:150px;font-size:3.6px;line-height:1.5;color:var(--blue-200)}
.cover .meta{position:absolute;left:16px;bottom:20px;font-size:3.4px;line-height:1.7;color:var(--blue-100)}
.inner{width:200px;padding:12px 14px}
.p2{left:200px}.p3{left:400px}.p4{left:600px}.p5{left:800px}.p6{left:1000px}
h2{font-family:"Playfair Display",Georgia,serif;font-size:6px;color:var(--blue-900);font-weight:600;margin-bottom:5px}
h3{font-size:4.2px;color:var(--blue-900);font-weight:700;margin:6px 0 3px}
p{font-size:3.4px;line-height:1.55;margin-bottom:4px}
.photo{border-radius:1px}
.ph-team{background:linear-gradient(135deg,var(--blue-400),var(--blue-200) 60%,var(--pink-200))}
.ph-office{background:linear-gradient(135deg,var(--blue-200),var(--blue-700))}
.ph-agent{background:linear-gradient(160deg,var(--blue-100),var(--blue-400))}
.ph-portrait{background:linear-gradient(180deg,var(--blue-200),var(--blue-700))}
.row{display:flex;gap:6px;align-items:flex-start}
.team{display:flex;gap:5px;margin:4px 0 3px}
.member{width:38px;text-align:center;font-size:3px;color:var(--muted)}
.member .photo{height:30px;margin-bottom:2px}
.cost{width:100%;border-collapse:collapse;font-size:3.2px;margin-top:4px}
.cost th{text-align:left;color:var(--blue-900);font-weight:700;border-bottom:.5px solid var(--blue-400);padding:1.5px 0}
.cost td{border-bottom:.5px solid var(--rule);padding:2px 0}
.sign{display:flex;gap:8px;margin:2px 0 12px}
.field{flex:1;font-size:3.2px;color:var(--muted)}
.field .line{height:7px;border:.5px solid var(--blue-200);margin-top:2px;background:var(--blue-100)}
</style>
</head>
<body>

<section class="page cover">
  <div class="brand">Harbor Line</div>
  <h1>Business Proposal Template for [Client.Company]</h1>
  <p class="lede">Prepared by Harbor Line for your review, covering services, team and costs.</p>
  <div class="meta">
    Prepared by: Jane Doe<br>
    Company: Harbor Line<br>
    Date: 01/01/2025<br>
    Phone: 555 0100<br>
    Email: hello@harborline.example
  </div>
  <div class="cover-band"></div>
</section>

<section class="page inner p2">
  <h2>Company Overview</h2>
  <div class="photo ph-team" style="height:52px;margin-bottom:6px" role="img" aria-label="Photo of the call center team at work"></div>
  <p>Harbor Line handles customer service for banks and credit unions with trained agents, secure systems and clear reporting every day.</p>
  <div class="row" style="margin:6px 0">
    <div class="photo ph-office" style="width:80px;height:44px;flex:none" role="img" aria-label="Photo of the office floor"></div>
    <p>Our team answers calls, chats and emails around the clock.</p>
  </div>
  <p>We build trust for every client through calm, accurate support.</p>
</section>

<section class="page inner p3">
  <h2>Recently Released</h2>
  <div class="row" style="margin-bottom:5px">
    <div class="photo ph-agent" style="width:80px;height:50px" role="img" aria-label="Photo of an agent with a headset"></div>
    <div class="photo ph-office" style="width:86px;height:50px" role="img" aria-label="Photo of a support specialist"></div>
  </div>
  <div class="row">
    <p style="width:80px">New service lines for card support and loan questions.</p>
    <p style="width:86px">Extended hours for account and payment help desks.</p>
  </div>
  <div class="row" style="margin-top:10px">
    <p style="width:80px">Faster onboarding for new financial partners this year.</p>
    <div class="photo ph-team" style="width:86px;height:52px" role="img" aria-label="Photo of a customer service agent"></div>
  </div>
</section>

<section class="page inner p4">
  <h2>About Proposal</h2>
  <p>This proposal outlines how our agents will support your customers, meet service levels and protect data.</p>
  <h3>Our Team</h3>
  <div class="team">
    <div class="member"><div class="photo ph-portrait" role="img" aria-label="Team member portrait"></div>Name Surname</div>
    <div class="member"><div class="photo ph-portrait" role="img" aria-label="Team member portrait"></div>Name Surname</div>
    <div class="member"><div class="photo ph-portrait" role="img" aria-label="Team member portrait"></div>Name Surname</div>
    <div class="member"><div class="photo ph-portrait" role="img" aria-label="Team member portrait"></div>Name Surname</div>
  </div>
  <p>Each team lead owns quality, training and weekly reports for your account.</p>
</section>

<section class="page inner p5">
  <h2>Scope of Work</h2>
  <p>We manage inbound calls, outbound follow-ups and digital channels for your customers.</p>
  <p>Scripts, escalation paths and reports are agreed before launch.</p>
  <p>Service runs in three phases over twelve weeks.</p>
  <h3>Cost and Timings</h3>
  <p>Pricing below covers setup and monthly service.</p>
  <table class="cost">
    <tr><th>Item</th><th>Rate</th><th>Total</th></tr>
    <tr><td>Setup</td><td>$0.00</td><td>$0.00</td></tr>
    <tr><td>Monthly</td><td>$0.00</td><td>$0.00</td></tr>
  </table>
</section>

<section class="page inner p6">
  <h2>Signature Section</h2>
  <div class="sign">
    <div class="field">Prepared by<div class="line"></div></div>
    <div class="field">Client Name<div class="line"></div></div>
  </div>
  <h3>Approval</h3>
  <p>By signing below both parties accept the terms of this proposal.</p>
</section>

</body>
</html>
```